Hal's Remedies Business Card Design Project

I need a business card designed for my pharmacy Hal's Remedies. I would like just the logo on one side, maybe with black background and white lettering. The other side I would also like to include my logo which is attached. Also, please include my name and the following information:
Hal Norwick Owner/Pharm D.
Business address is 7163 N Birch Rd Sioux Falls, SD 57291.
Phone number is 605-318-6027 and fax # is 605-318-6031.
my email address is hal@halsremedies.example.
My website is www.halsremedies.example.
My business hours are Monday-Friday 8am-7 pm. Saturday 8am-12 pm. Sunday Closed.
I would like the design to include my logo colors, black, white, and neon green. Silver may be added as a highlight. Thanks.
Pharmacy
See above in product description

```html
<!DOCTYPE html>
<html lang="en">
<head>
<meta charset="utf-8">
<title>Hal's Remedies – Business Card</title>
<link href="https://fonts.googleapis.com/css2?family=Open+Sans:ital,wght@0,400;0,700;1,700&display=swap" rel="stylesheet">
<style>
  :root {
    --card: #3a3a3a;
    --band: #242424;
    --frame: #262626;
    --cell: #444444;
    --stripe: #4a4a4a;
    --white: #ffffff;
    --text: #f2f2f2;
    --green: #8cc63f;
  }
  * { margin: 0; padding: 0; box-sizing: border-box; }
  html, body { width: 988px; height: 1200px; overflow: hidden; background: var(--card); }
  body { position: relative; font-family: "Open Sans", Arial, sans-serif; color: var(--text); }

  .card { position: absolute; left: 0; width: 988px; background: var(--card); overflow: hidden; }
  .card-front { top: 0; height: 528px; }
  .card-back { top: 604px; height: 527px; }

  .rule { position: absolute; left: 0; width: 988px; height: 5px; background: var(--white); }
  .stripe-band { position: absolute; left: 0; width: 988px; background: var(--stripe); }

  .brand-dot { position: absolute; border-radius: 50%; background: var(--green); }
  .brand-divider { position: absolute; width: 4px; background: var(--white); }
  .brand-name { position: absolute; font-weight: 700; color: var(--white); letter-spacing: -1.5px; white-space: nowrap; }
  .brand-url { position: absolute; font-weight: 700; font-style: italic; color: var(--white); white-space: nowrap; font-size: 25px; }

  .info-band { position: absolute; left: 0; width: 988px; background: var(--band); }
  .hours-frame { position: absolute; left: 67px; top: 256px; width: 232px; height: 233px; background: var(--frame); }
  .hours-cell { position: absolute; left: 12px; width: 210px; height: 40px; background: var(--cell);
    font-size: 23px; line-height: 40px; padding-left: 6px; white-space: nowrap; overflow: hidden; }
  .hours-title { text-align: center; padding-left: 0; }

  .contact-name { position: absolute; left: 312px; top: 271px; font-size: 24px; line-height: 38px; white-space: nowrap; }
  .contact-line { position: absolute; left: 312px; font-size: 17px; line-height: 38px; white-space: nowrap; }
  .contact-line svg { vertical-align: middle; margin-right: 14px; }
</style>
</head>
<body>
  <section class="card card-front">
    <div class="brand-dot" style="left:260px; top:263px; width:60px; height:60px;"></div>
    <div class="brand-divider" style="left:359px; top:231px; height:122px;"></div>
    <div class="brand-name" style="left:396px; top:248px; font-size:61px; line-height:70px;">Hal's Remedies</div>
    <div class="brand-url" style="right:159px; top:322px;">www.halsremedies.example</div>
  </section>

  <div class="rule" style="top:528px;"></div>
  <div class="stripe-band" role="img" aria-label="Diagonal striped divider band" style="top:533px; height:66px;"></div>
  <div class="rule" style="top:599px;"></div>

  <section class="card card-back">
    <div class="brand-dot" style="left:128px; top:90px; width:56px; height:56px;"></div>
    <div class="brand-divider" style="left:214px; top:69px; height:100px;"></div>
    <div class="brand-name" style="left:244px; top:86px; font-size:52px; line-height:60px;">Hal's Remedies</div>

    <div class="info-band" style="top:273px; height:38px;"></div>
    <div class="info-band" style="top:324px; height:38px;"></div>
    <div class="info-band" style="top:372px; height:38px;"></div>
    <div class="info-band" style="top:420px; height:40px;"></div>

    <div class="hours-frame">
      <div class="hours-cell hours-title" style="top:12px;">Business Hours</div>
      <div class="hours-cell" style="top:59px;">Mon-Fri: 8am-7pm</div>
      <div class="hours-cell" style="top:109px;">Sat: 8am-12pm</div>
      <div class="hours-cell" style="top:158px;">Sunday: CLOSED</div>
    </div>

    <div class="contact-name">Hal Norwick Owner/Pharm D.</div>
    <div class="contact-line" style="top:324px;"><svg width="8" height="12" viewBox="0 0 8 12"><path d="M0 0 L8 6 L0 12 Z" fill="#fff"/></svg>7163 N Birch Rd Sioux Falls, SD 57291</div>
    <div class="contact-line" style="top:372px;"><svg width="8" height="12" viewBox="0 0 8 12"><path d="M0 0 L8 6 L0 12 Z" fill="#fff"/></svg>Tel: 605-318-6027 , Fax: 605-318-6031</div>
    <div class="contact-line" style="top:421px;"><svg width="8" height="12" viewBox="0 0 8 12"><path d="M0 0 L8 6 L0 12 Z" fill="#fff"/></svg>www.halsremedies.example &amp; hal@halsremedies.example</div>
  </section>

  <div class="rule" style="top:1131px;"></div>
  <div class="stripe-band" role="img" aria-label="Diagonal striped divider band" style="top:1136px; height:64px;"></div>
</body>
</html>
```